"Hvarfa Frændur" ( icelandic rap group needs a album cover front and back with ...

Hello everybody we need an album cover for our upcoming project and since its our debut album we would just like the band name to be the name of the album ( Hvarfa Frændur ) we would like to see a kind of animated version of our selves for instance or just something cool that you can think of using these photos.we would like to see the colours black, lightblue and purple being used but thats just and idea, nothing thats nessecaryHere is the tracklist in correct order that should be on the backside 1. Sit Kyrr 2. Dorwin 3.Miðar4.Pushertown5.Emminalex6.Svartur á Leik7. Kalmo(remake)8.Réttar Ranghugmyndir9.Joy10. TPRK(remake) This is going to be printed on what they call a cd digipak so it would be lovely to get something in similar design for the inside of the cd digipak aswell
we are mainly looking for a kind of animated versions of our selves

```html
<!DOCTYPE html>
<html lang="is">
<head>
<meta charset="utf-8">
<title>Hvarfa Frændur – Digipak</title>
<link href="https://fonts.googleapis.com/css2?family=Archivo+Black&family=Montserrat:wght@400;800&display=swap" rel="stylesheet">
<style>
  :root {
    --board-light: #f1f1f1;
    --board-dark: #c4c4c4;
    --ink: #000000;
    --paper: #ffffff;
    --photo-light: #f7f7f7;
    --photo-mid: #d9d9d9;
    --photo-dark: #1c1c1c;
  }
  html, body { margin: 0; padding: 0; overflow: hidden; }
  .board {
    position: relative;
    width: 1200px;
    height: 857px;
    overflow: hidden;
    background: linear-gradient(135deg, var(--board-light) 0%, var(--board-dark) 100%);
    font-family: "Montserrat", sans-serif;
  }
  .wordmark {
    position: absolute;
    left: 93px;
    top: 116px;
    margin: 0;
    font-family: "Archivo Black", sans-serif;
    font-weight: 400;
    font-size: 17px;
    line-height: 0.98;
    letter-spacing: -0.3px;
    color: var(--ink);
  }
  .digipak {
    position: absolute;
    left: 71px;
    top: 224px;
    width: 1047px;
    height: 479px;
    display: flex;
    box-shadow: 3px 4px 5px rgba(0,0,0,0.35);
  }
  .back-panel {
    position: relative;
    width: 509px;
    height: 100%;
    background: var(--ink);
    overflow: hidden;
  }
  .spine {
    position: relative;
    width: 27px;
    height: 100%;
    background: var(--ink);
    border-left: 1px solid #222;
    border-right: 1px solid #222;
    box-sizing: border-box;
  }
  .front-panel {
    position: relative;
    flex: 1;
    height: 100%;
    overflow: hidden;
    background: var(--paper);
  }
  .tracklist {
    position: absolute;
    left: 46px;
    top: 258px;
    margin: 0;
    padding: 0;
    list-style: none;
    color: var(--paper);
    font-size: 10.5px;
    line-height: 18.2px;
  }
  .album-title {
    position: absolute;
    margin: 0;
    writing-mode: vertical-rl;
    transform: rotate(180deg);
    font-family: "Archivo Black", sans-serif;
    font-weight: 400;
    font-size: 74px;
    line-height: 0.98;
    letter-spacing: -1px;
    white-space: nowrap;
  }
  .album-title span { display: block; }
  .album-title--back { left: 283px; bottom: 22px; color: var(--paper); }
  .album-title--front { left: 202px; bottom: 14px; color: var(--ink); }
  .spine-title {
    position: absolute;
    left: 50%;
    bottom: 24px;
    writing-mode: vertical-rl;
    transform: translateX(-50%) rotate(180deg);
    font-family: "Montserrat", sans-serif;
    font-weight: 800;
    font-size: 9px;
    letter-spacing: 0.3px;
    color: var(--paper);
    white-space: nowrap;
  }
  .portrait {
    position: absolute;
    bottom: 0;
  }
  .portrait--left {
    left: 0;
    width: 212px;
    height: 348px;
    background: linear-gradient(180deg, var(--photo-dark) 0%, #2e2e2e 30%, var(--photo-mid) 55%, #111 100%);
  }
  .portrait--right {
    right: 0;
    width: 158px;
    height: 323px;
    background: linear-gradient(180deg, var(--photo-dark) 0%, #2e2e2e 30%, var(--photo-mid) 55%, #222 100%);
  }
</style>
</head>
<body>
<main class="board">
  <p class="wordmark">HVARFA<br>FRÆNDUR</p>

  <section class="digipak">
    <div class="back-panel">
      <ol class="tracklist">
        <li>1. Sit Kyrr</li>
        <li>2. Dorwin</li>
        <li>3. Fánar</li>
        <li>4. Drifterdale</li>
        <li>5. Rodanifex</li>
        <li>6. Grænn í Skugga</li>
        <li>7. Kalmo(remake)</li>
        <li>8. Hljóðar Sólarstundir</li>
        <li>9. Fay</li>
        <li>10. TPRK(remake)</li>
      </ol>
      <h2 class="album-title album-title--back"><span>HVARFA</span><span>FRÆNDUR</span></h2>
    </div>

    <div class="spine">
      <span class="spine-title">HVARFA FRÆNDUR</span>
    </div>

    <div class="front-panel">
      <div class="portrait portrait--left" role="img" aria-label="Black and white photo of a rapper in a baseball cap and sunglasses looking down"></div>
      <div class="portrait portrait--right" role="img" aria-label="Black and white photo of a second rapper in a baseball cap and sunglasses looking down"></div>
      <h1 class="album-title album-title--front"><span>HVARFA</span><span>FRÆNDUR</span></h1>
    </div>
  </section>
</main>
</body>
</html>
```